KWT Contracting services . Building and maintenance services, optic fibre installation

Business cards and logo design.I need a logo that I can use on business cards ,workwear and on my vehicles. I would like the KWT to be the main or larger text and contracting services to be the smaller or less important text.I like monograms, modern designs and repeating patterns symbols. I am also a Gemini and my favourite number is 22 so if this can be any inspiration to help with the design. Am thinking of the using German flag colours as a his is my family’s heritage. And the other 2 main colours I wear is black and white.But any ideas are appreciated.I do not need a design that is trade specific but a design that could be used for any business.

Target Market(s)

General public

Contact Information for Business Card

KWT Contracting Services ( front of business card)

(Back of business card)
Milo Brackwood
0471539264
Maintenance services
Optic fibre and data installation

Logo Text

Logo can just be pattern or monogram or incorporate KWT . I like the gemini star sign and the number 22

Colors
ec1f27
000000
fbee3e
ffffff

Requirements
Must have
• Logo and KWT Contracting Services on the front of business card
Nice to have
• Possible use of German flag colours.
• Modern design.
• Design to be able to be used on black or white background as I want to put it on clothing

```html
<!DOCTYPE html>
<html lang="en">
<head>
<meta charset="UTF-8">
<title>KWT Contracting Services – Business Cards</title>
<link rel="stylesheet" href="https://fonts.googleapis.com/css2?family=Open+Sans:wght@400&family=Roboto:wght@700&display=swap">
<style>
  :root {
    --backdrop: #7d4a25;
    --kraft-light: #dcb584;
    --kraft-mid: #c89a66;
    --kraft-dark: #b3834f;
    --ink: #111111;
  }
  * { margin: 0; padding: 0; box-sizing: border-box; }
  html, body {
    width: 1200px;
    height: 900px;
    overflow: hidden;
  }
  body {
    position: relative;
    background: var(--backdrop);
  }
  .card {
    position: absolute;
    width: 556px;
    height: 343px;
    background: linear-gradient(160deg, var(--kraft-light) 0%, var(--kraft-mid) 45%, var(--kraft-dark) 100%);
    box-shadow: 3px 4px 6px rgba(0, 0, 0, 0.45);
    color: var(--ink);
  }
  .card--back { left: 330px; top: 90px; }
  .card--front { left: 330px; top: 469px; }

  .contact {
    position: absolute;
    left: 0;
    right: 0;
    top: 107px;
    text-align: center;
  }
  .contact__name {
    font-family: "Roboto", Arial, sans-serif;
    font-weight: 700;
    font-size: 19px;
    letter-spacing: 0.2px;
    line-height: 22px;
  }
  .contact__phone {
    font-family: "Open Sans", Arial, sans-serif;
    font-size: 19px;
    line-height: 30px;
    letter-spacing: 0.5px;
  }
  .contact__rule {
    width: 196px;
    height: 1px;
    margin: 14px auto 22px;
    background: var(--ink);
    border: 0;
  }
  .contact__services {
    font-family: "Open Sans", Arial, sans-serif;
    font-size: 15.5px;
    line-height: 19px;
    list-style: none;
  }

  .brand {
    position: absolute;
    left: 110px;
    top: 116px;
    display: flex;
    align-items: center;
    gap: 20px;
  }
  .brand__mark {
    width: 110px;
    height: 110px;
    display: block;
  }
  .brand__name {
    font-family: "Roboto", Arial, sans-serif;
    font-weight: 700;
    color: var(--ink);
  }
  .brand__initials {
    display: block;
    font-size: 88px;
    line-height: 74px;
    letter-spacing: 10px;
  }
  .brand__tagline {
    display: block;
    font-size: 16.5px;
    line-height: 20px;
    margin-top: 4px;
    text-transform: uppercase;
  }
</style>
</head>
<body>
  <section class="card card--back" aria-label="Business card back">
    <div class="contact">
      <p class="contact__name">MILO BRACKWOOD</p>
      <p class="contact__phone">0471539264</p>
      <hr class="contact__rule">
      <ul class="contact__services">
        <li>Maintenance services</li>
        <li>Optic fibre and data installation</li>
      </ul>
    </div>
  </section>

  <section class="card card--front" aria-label="Business card front">
    <div class="brand">
      <svg class="brand__mark" viewBox="0 0 110 110" aria-hidden="true">
        <rect x="20" y="20" width="70" height="70" fill="#111111"/>
      </svg>
      <p class="brand__name">
        <span class="brand__initials">KWT</span>
        <span class="brand__tagline">Contracting Services</span>
      </p>
    </div>
  </section>
</body>
</html>
```